Sensual cosmetic range, design logo and box

This is a new sub brand under the Velaroze Range of cosmetics. Velaroze is a "Glow from Inside" range of approx 30 existing products.

This new range will consist of four products initially. I am seeking an innovative look and feel for this new sub brand of sensual cosmetics products. I have uploaded two pdfs of the box for the designs to be done on . I would like the designer to design the look and feel, colours etc and name of the range (all we have is the word sensual so the designer can use that name or it can be a entirely new name as long as it portrays the word sensual in it"

This particular product is sensual massage cream. I have supplied the box dimension on the pdf( one square and one rectangular.)

Target Market(s)

female only, between the ages of 24 to 49

Industry/Entity Type

Cosmetics

Requirements
Must have
• A name and design for the new range plus colours. Currently all we have is the name "sensuals". I am not stuck on this name and we are happy to see a new name. As long as the name, design and colour portrays " sensual or sensuality "

I have also supplied the existing Velaroze logo. I will leave it up to the designer interpretation if they want the existing velaroze logo to dominate or it can be made small and not prominent at all. it can even be made black and white .

the right colour combination. The containers I am using and packaging is all white, silver and clear. the box should go with these colours and also have a senual look and feel

keep in mind it is a women's range only

```html
<!DOCTYPE html>
<html lang="en">
<head>
<meta charset="utf-8">
<title>Velaroze Sensual Massage Cream – Box Front</title>
<link rel="stylesheet" href="https://fonts.googleapis.com/css2?family=Arimo:wght@400&family=Playfair+Display:ital,wght@1,700&display=swap">
<style>
  :root {
    --backdrop: #e9e9ea;
    --panel: #ffffff;
    --panel-shade: #f6f6f7;
    --brand-pink: #d2185f;
    --blush: #f6d4e0;
    --blush-soft: #fbe9ef;
    --silver: #a9a9ab;
    --silver-dark: #8e8e91;
    --ink-grey: #8a8a8c;
  }
  * { box-sizing: border-box; margin: 0; padding: 0; }
  html, body {
    width: 1005px;
    height: 1200px;
    overflow: hidden;
    background: var(--backdrop);
  }
  .canvas {
    position: relative;
    width: 1005px;
    height: 1200px;
  }
  .box-front {
    position: absolute;
    left: 287px;
    top: 50px;
    width: 430px;
    height: 1100px;
    background: linear-gradient(90deg, var(--panel) 0%, var(--panel) 70%, var(--panel-shade) 100%);
    box-shadow: 0 2px 10px rgba(0, 0, 0, 0.12);
    overflow: hidden;
  }
  .ornament {
    position: absolute;
    display: block;
  }
  .ornament--top-right {
    right: -40px;
    top: 40px;
    width: 300px;
    height: 520px;
  }
  .ornament--lower-left {
    left: -60px;
    top: 430px;
    width: 260px;
    height: 420px;
  }
  .brand {
    position: absolute;
    left: 0;
    right: 0;
    top: 330px;
    display: flex;
    justify-content: center;
    align-items: center;
    gap: 10px;
  }
  .brand__dot {
    width: 22px;
    height: 22px;
    border-radius: 50%;
    background: var(--brand-pink);
  }
  .brand__name {
    font-family: "Arimo", Arial, sans-serif;
    font-weight: 400;
    font-size: 30px;
    color: var(--brand-pink);
    letter-spacing: 0.5px;
  }
  .range-name {
    position: absolute;
    left: 0;
    right: 0;
    top: 480px;
    text-align: center;
    font-family: "Playfair Display", Georgia, serif;
    font-style: italic;
    font-weight: 700;
    font-size: 76px;
    color: var(--silver);
    letter-spacing: 1px;
    text-shadow: 0 1px 0 #ffffff, 0 2px 2px rgba(0, 0, 0, 0.12);
  }
  .product-name {
    position: absolute;
    left: 0;
    right: 0;
    top: 594px;
    text-align: center;
    font-family: "Arimo", Arial, sans-serif;
    font-size: 30px;
    color: var(--silver-dark);
    letter-spacing: 0.5px;
  }
  .volume {
    position: absolute;
    left: 0;
    right: 0;
    top: 915px;
    text-align: center;
    font-family: "Arimo", Arial, sans-serif;
    font-size: 26px;
    color: var(--ink-grey);
  }
</style>
</head>
<body>
<main class="canvas">
  <section class="box-front">
    <svg class="ornament ornament--top-right" role="img" aria-label="Soft pink floral swirl ornament" viewBox="0 0 300 520">
      <defs>
        <radialGradient id="blushTop" cx="60%" cy="40%" r="60%">
          <stop offset="0%" stop-color="var(--blush)" stop-opacity="0.85"/>
          <stop offset="100%" stop-color="var(--blush-soft)" stop-opacity="0"/>
        </radialGradient>
      </defs>
      <rect width="300" height="520" fill="url(#blushTop)"/>
    </svg>
    <svg class="ornament ornament--lower-left" role="img" aria-label="Faint pink floral ornament" viewBox="0 0 260 420">
      <defs>
        <radialGradient id="blushLow" cx="30%" cy="55%" r="60%">
          <stop offset="0%" stop-color="var(--blush-soft)" stop-opacity="0.9"/>
          <stop offset="100%" stop-color="var(--blush-soft)" stop-opacity="0"/>
        </radialGradient>
      </defs>
      <rect width="260" height="420" fill="url(#blushLow)"/>
    </svg>

    <div class="brand">
      <span class="brand__dot"></span>
      <span class="brand__name">Velaroze</span>
    </div>
    <h1 class="range-name">Sensual</h1>
    <p class="product-name">MASSAGE CREAM</p>
    <p class="volume">150 ml</p>
  </section>
</main>
</body>
</html>
```